Bellcrest HVAC Business Card design

Looking for a modern professional two sided design. Showing contact info and services provided. Possibly on a silk card stock.
Using blues or greens or greys and maybe metallic. One color or a mixture of these.
Dorian Vance
dvance@bellcresthvac-example.net
555-318-4702
Air Conditioning
Heating
Heat Pumps / Gas / Oil
Ductless mini splits
Controls
VFD's
Pumps
Gas Fitting/Piping
Service and New install
Residential / Commercial
Industry/Entity Type
Mechanical HVAC
Contact Information for Business Card
Logo, contact info and provided services

```html
<!DOCTYPE html>
<html lang="en">
<head>
<meta charset="utf-8">
<title>Bellcrest HVAC Business Card</title>
<link href="https://fonts.googleapis.com/css2?family=Montserrat:wght@400;500;600;700&display=swap" rel="stylesheet">
<style>
  :root {
    --navy: #0a1f7a;
    --navy-deep: #071a6e;
    --royal: #1747a6;
    --cyan: #3ec6d6;
    --gold: #f2a81d;
    --gold-dark: #b87a0e;
    --white: #ffffff;
    --ink: #14208a;
    --backdrop: #dde3e5;
  }
  * { margin: 0; padding: 0; box-sizing: border-box; }
  html, body {
    width: 1200px; height: 1200px; overflow: hidden;
    background: var(--backdrop);
    font-family: "Montserrat", sans-serif;
  }
  .card {
    position: absolute; left: 276px; width: 649px; height: 370px; overflow: hidden;
    background: var(--white);
  }
  .card-front { top: 185px; }
  .card-back { top: 642px; }

  /* Front */
  .front-field {
    position: absolute; left: 0; top: 0; width: 100%; height: 316px;
    background: radial-gradient(ellipse 260px 230px at 50% 72%, var(--cyan) 0%, #1f82c0 40%, var(--royal) 70%, var(--navy) 100%);
  }
  .front-rule {
    position: absolute; left: 0; top: 311px; width: 100%; height: 6px; background: var(--gold);
  }
  .front-brand {
    position: absolute; left: 0; top: 120px; width: 100%; text-align: center;
    color: var(--white); font-weight: 700; font-size: 46px; letter-spacing: 1px;
  }
  .service-icons { position: absolute; left: 0; top: 0; }

  /* Back */
  .back-panel {
    position: absolute; left: 362px; top: 0; width: 287px; height: 100%;
    background: radial-gradient(ellipse 220px 200px at 0% 72%, var(--cyan) 0%, #1f7fbf 40%, var(--royal) 70%, var(--navy-deep) 100%);
    border-left: 3px solid var(--gold);
  }
  .back-brand {
    position: absolute; left: 0; top: 92px; width: 362px; text-align: center;
    color: var(--ink); font-weight: 700; font-size: 28px;
  }
  .contact-name {
    position: absolute; left: 73px; top: 203px; font-size: 28px; color: var(--ink); font-weight: 400;
  }
  .contact-name strong { font-weight: 700; }
  .contact-line {
    position: absolute; left: 73px; display: flex; align-items: center; gap: 10px; color: var(--ink);
  }
  .contact-phone { top: 242px; font-size: 19px; font-weight: 700; }
  .contact-email { top: 273px; font-size: 12.5px; font-weight: 500; }
  .contact-line svg { flex: none; }

  .service-list { position: absolute; left: 351px; top: 36px; list-style: none; }
  .service-list li {
    display: flex; align-items: center; gap: 10px; height: 30px;
    color: var(--white); font-size: 18px; font-weight: 500; letter-spacing: 0.3px;
  }
</style>
</head>
<body>

<section class="card card-front" aria-label="Card front">
  <div class="front-field"></div>
  <div class="front-rule"></div>
  <div class="front-brand">Bellcrest HVAC</div>
  <svg class="service-icons" width="649" height="370" viewBox="0 0 649 370" aria-label="Service icons: air, cooling, water, heat">
    <defs>
      <radialGradient id="goldCoin" cx="50%" cy="40%" r="60%">
        <stop offset="0%" stop-color="#f8e2a6"/>
        <stop offset="45%" stop-color="#e6a33a"/>
        <stop offset="100%" stop-color="#a86b10"/>
      </radialGradient>
    </defs>
    <g fill="url(#goldCoin)">
      <circle cx="190" cy="313" r="27"/>
      <circle cx="279" cy="313" r="27"/>
      <circle cx="369" cy="313" r="27"/>
      <circle cx="459" cy="313" r="27"/>
    </g>
    <g fill="none" stroke="#fff" stroke-width="3" stroke-linecap="round">
      <path d="M176 305 h20 a5 5 0 1 0 -5 -5"/>
      <path d="M176 313 h26 a5 5 0 1 1 -5 5"/>
      <path d="M180 321 h10"/>
    </g>
    <g stroke="#fff" stroke-width="3" stroke-linecap="round">
      <path d="M279 299 v28 M267 306 l24 14 M267 320 l24 -14"/>
    </g>
    <path d="M369 299 C363 309 359 314 359 319 a10 10 0 0 0 20 0 C379 314 375 309 369 299 Z" fill="#fff"/>
    <path d="M459 298 c3 8 11 12 11 22 a11 11 0 0 1 -22 0 c0 -5 3 -8 5 -10 c0 4 2 6 4 6 c0 -6 -1 -12 2 -18 Z" fill="#fff"/>
  </svg>
</section>

<section class="card card-back" aria-label="Card back">
  <div class="back-brand">Bellcrest HVAC</div>
  <div class="contact-name"><strong>Dorian</strong> Vance</div>
  <div class="contact-line contact-phone">
    <svg width="18" height="18" viewBox="0 0 24 24"><path d="M6.6 10.8c1.4 2.8 3.8 5.1 6.6 6.6l2.2-2.2c.3-.3.7-.4 1-.2 1.1.4 2.3.6 3.6.6.6 0 1 .4 1 1V20c0 .6-.4 1-1 1C10.6 21 3 13.4 3 4c0-.6.4-1 1-1h3.5c.6 0 1 .4 1 1 0 1.3.2 2.5.6 3.6.1.3 0 .7-.2 1L6.6 10.8z" fill="var(--gold)"/></svg>
    555-318-4702
  </div>
  <div class="contact-line contact-email">
    <svg width="18" height="14" viewBox="0 0 18 14"><rect width="18" height="14" rx="1.5" fill="var(--gold)"/><path d="M1 1.5 L9 8 L17 1.5" fill="none" stroke="#fff" stroke-width="1.6"/></svg>
    dvance@bellcresthvac-example.net
  </div>

  <div class="back-panel"></div>
  <ul class="service-list">
    <li><svg width="22" height="22" viewBox="0 0 22 22"><circle cx="11" cy="11" r="11" fill="var(--gold)"/><path d="M6.5 11.2 L9.6 14 L15.5 8" fill="none" stroke="#fff" stroke-width="2.2" stroke-linecap="round" stroke-linejoin="round"/></svg>Air Conditioning</li>
    <li><svg width="22" height="22" viewBox="0 0 22 22"><circle cx="11" cy="11" r="11" fill="var(--gold)"/><path d="M6.5 11.2 L9.6 14 L15.5 8" fill="none" stroke="#fff" stroke-width="2.2" stroke-linecap="round" stroke-linejoin="round"/></svg>Heating</li>
    <li><svg width="22" height="22" viewBox="0 0 22 22"><circle cx="11" cy="11" r="11" fill="var(--gold)"/><path d="M6.5 11.2 L9.6 14 L15.5 8" fill="none" stroke="#fff" stroke-width="2.2" stroke-linecap="round" stroke-linejoin="round"/></svg>Heat Pump / Gas / Oil</li>
    <li><svg width="22" height="22" viewBox="0 0 22 22"><circle cx="11" cy="11" r="11" fill="var(--gold)"/><path d="M6.5 11.2 L9.6 14 L15.5 8" fill="none" stroke="#fff" stroke-width="2.2" stroke-linecap="round" stroke-linejoin="round"/></svg>Ductless mini splits</li>
    <li><svg width="22" height="22" viewBox="0 0 22 22"><circle cx="11" cy="11" r="11" fill="var(--gold)"/><path d="M6.5 11.2 L9.6 14 L15.5 8" fill="none" stroke="#fff" stroke-width="2.2" stroke-linecap="round" stroke-linejoin="round"/></svg>Controls</li>
    <li><svg width="22" height="22" viewBox="0 0 22 22"><circle cx="11" cy="11" r="11" fill="var(--gold)"/><path d="M6.5 11.2 L9.6 14 L15.5 8" fill="none" stroke="#fff" stroke-width="2.2" stroke-linecap="round" stroke-linejoin="round"/></svg>VFD's</li>
    <li><svg width="22" height="22" viewBox="0 0 22 22"><circle cx="11" cy="11" r="11" fill="var(--gold)"/><path d="M6.5 11.2 L9.6 14 L15.5 8" fill="none" stroke="#fff" stroke-width="2.2" stroke-linecap="round" stroke-linejoin="round"/></svg>Pumps</li>
    <li><svg width="22" height="22" viewBox="0 0 22 22"><circle cx="11" cy="11" r="11" fill="var(--gold)"/><path d="M6.5 11.2 L9.6 14 L15.5 8" fill="none" stroke="#fff" stroke-width="2.2" stroke-linecap="round" stroke-linejoin="round"/></svg>Gas Fitting / Piping</li>
    <li><svg width="22" height="22" viewBox="0 0 22 22"><circle cx="11" cy="11" r="11" fill="var(--gold)"/><path d="M6.5 11.2 L9.6 14 L15.5 8" fill="none" stroke="#fff" stroke-width="2.2" stroke-linecap="round" stroke-linejoin="round"/></svg>Service and New install</li>
    <li><svg width="22" height="22" viewBox="0 0 22 22"><circle cx="11" cy="11" r="11" fill="var(--gold)"/><path d="M6.5 11.2 L9.6 14 L15.5 8" fill="none" stroke="#fff" stroke-width="2.2" stroke-linecap="round" stroke-linejoin="round"/></svg>Residential / Commercial</li>
  </ul>
</section>

</body>
</html>
```